Redesign iOS App UI and Graphics

I'm looking to update my apps UI and graphics. Please see link below:
The contest winner will need all the scenes to be redesigned and submitted for final release of payment, but for the contest submission please re-design the scenes on the attached images and I will pick a winner from there. After a winner is picked, you will need to finish the other scenes and I will submit final payment when complete.
The app is currently in blue and white colors but we do NOT have to use these colors. We can use different idea so please submit what you think will look nice.
Also, if you feel like a landscape UI would be better for this app, then I would also consider that too.
The pixel dimensions should be 1242 x 2208 (or 2208 x 1242).
I prefer the final graphics to be sent in Photoshop with layers of each item so that it can be edited later if needed.
Thanks

```html
<!DOCTYPE html>
<html lang="en">
<head>
<meta charset="utf-8">
<title>Daily Clips – Light and Dark UI</title>
<link href="https://fonts.googleapis.com/css2?family=Open+Sans:wght@400;600;700&family=Ubuntu:wght@500;700&display=swap" rel="stylesheet">
<style>
:root{
  --pink:#f7516a;--coral:#fb7d60;
  --accent:linear-gradient(90deg,#f7516a,#fb7d60);
  --day:linear-gradient(160deg,#f9606a,#fb7c5e);
  --ui:"Open Sans",Arial,sans-serif;--display:"Ubuntu","Open Sans",sans-serif;
}
*{box-sizing:border-box;margin:0;padding:0}
html,body{width:1200px;height:4820px;overflow:hidden}
body{position:relative;font-family:var(--ui)}
.board{position:absolute;left:0;width:1200px}
.board--light{top:0;height:2411px;background:linear-gradient(160deg,#f6506d 0%,#f96a67 45%,#fb8a63 100%);
  --screen:#fff;--text:#2b2b2b;--sub:#8d8d8d;--line:#ececec;--field:#fff;--fieldline:#dedede;--chip:#e9e9e9;--chipico:#333;--tab:#fff;--r1:153px;--lbl:1002px;--r2:1134px;--ttl:42px}
.board--dark{top:2411px;height:2409px;background:#1e2232;
  --screen:#292d3e;--text:#fff;--sub:#b9bcc8;--line:#343849;--field:#30344a;--fieldline:#3c4056;--chip:#3a3e53;--chipico:#e6e7ee;--tab:#262a3a;--r1:199px;--lbl:1050px;--r2:1179px;--ttl:88px}
.board__title{position:absolute;left:94px;top:var(--ttl);font:700 54px var(--display);color:#fff}
.board__size{position:absolute;left:505px;top:calc(var(--ttl) + 22px);font:500 29px var(--display);color:#fff}
.board__label{position:absolute;top:var(--lbl);width:464px;text-align:center;font:700 31px var(--display);color:#fff}
.thanks{position:absolute;left:690px;top:2170px;font:700 68px var(--display);color:#fff}

.phone{position:absolute;width:464px;height:828px;background:var(--screen);border-radius:37px;overflow:hidden;color:var(--text);box-shadow:0 18px 40px rgba(0,0,0,.12)}
.phone--tall{height:1118px}
.slot-a{left:94px;top:var(--r1)}.slot-b{left:640px;top:var(--r1)}
.slot-c{left:94px;top:var(--r2)}.slot-d{left:640px;top:var(--r2)}
.label-a{left:94px}.label-b{left:640px}

.status{position:absolute;top:8px;left:26px;right:26px;height:16px;font:600 10px var(--ui);display:flex;justify-content:space-between;align-items:center}
.status__batt{display:inline-block;width:22px;height:9px;border-radius:2px;background:var(--text);vertical-align:middle;margin-left:4px}
.nav{position:absolute;top:28px;left:0;right:0;height:52px;border-bottom:2px solid var(--line);display:flex;align-items:center;justify-content:center}
.nav__menu{position:absolute;left:19px;top:16px;width:24px;height:20px}
.nav__back{position:absolute;left:18px;top:16px;width:18px;height:20px}
.nav__title{display:flex;align-items:center;gap:22px;font:700 26px var(--ui)}
.nav__title--small{font:700 19px var(--ui)}
.ico{width:14px;height:22px;stroke:var(--text);fill:none;stroke-width:3}

.toolbar{position:absolute;top:107px;left:19px;right:17px;display:flex;gap:19px}
.btn-fill{width:196px;height:43px;border-radius:22px;background:var(--accent);color:#fff;font:600 15px var(--ui);display:flex;align-items:center;justify-content:center;box-shadow:0 6px 12px rgba(247,81,106,.3)}
.viewas{flex:1;height:43px;border-radius:22px;border:2px solid var(--fieldline);display:flex;align-items:center;padding-left:26px;gap:18px;font:700 18px var(--ui)}
.viewas svg{width:26px;height:26px}

.grid{position:absolute;left:19px;right:17px;bottom:93px;display:grid;overflow:hidden;align-content:start}
.grid--two{top:176px;grid-template-columns:204px 204px;grid-auto-rows:230px;gap:21px 20px}
.grid--three{top:178px;grid-template-columns:repeat(3,131px);grid-auto-rows:135px;gap:22px 17px}
.tile{position:relative;border-radius:6px;overflow:hidden}
.photo-a{background:linear-gradient(165deg,#9cc1dc 0%,#c9b677 40%,#6b8f3b 75%,#a7b85a 100%)}
.photo-b{background:linear-gradient(160deg,#3e5a2a 0%,#b9c99a 35%,#8a7a5a 70%,#d6d0b0 100%)}
.photo-c{background:linear-gradient(170deg,#a9cbe6 0%,#e6cd7d 35%,#6fa43d 70%,#4f8a2a 100%)}
.tile__meta{position:absolute;left:0;right:0;bottom:0;height:42px;background:linear-gradient(transparent,rgba(0,0,0,.55));display:flex;align-items:flex-end;padding:0 10px 8px;color:#fff;gap:6px}
.tile__meta svg{width:16px;height:16px;fill:#fff}
.tile__num{font:700 26px/1 var(--ui)}
.tile__dow{font:600 10px/1 var(--ui);margin-bottom:2px}
.tile__end{margin-left:auto}
.grid--three .tile__meta{height:32px;padding:0 6px 5px;gap:4px}
.grid--three .tile__num{font-size:22px}
.grid--three .tile__meta svg{width:12px;height:12px}
.tile--day{background:var(--day);color:#fff;text-align:center}
.tile--day .cal{position:absolute;left:12px;top:12px;width:18px;height:18px;fill:rgba(255,255,255,.7)}
.day__num{position:absolute;left:0;right:0;top:44px;font:600 72px/1 var(--ui)}
.day__dow{position:absolute;left:0;right:0;top:118px;font:400 22px var(--ui)}
.day__add{position:absolute;left:46px;top:174px;width:108px;height:40px;border-radius:20px;background:#fff;color:var(--pink);font:600 15px var(--ui);display:flex;align-items:center;justify-content:center;gap:8px}
.day__add i,.plus{display:inline-flex;align-items:center;justify-content:center;width:20px;height:20px;border-radius:50%;background:var(--pink);color:#fff;font:700 16px/1 var(--ui);font-style:normal}
.grid--three .day__num{top:26px;font-size:56px}
.grid--three .day__dow{top:84px;font-size:19px}
.grid--three .plus{position:absolute;right:8px;bottom:8px;width:22px;height:22px;background:#fff;color:var(--pink)}
.grid--three .tile--day .cal{left:9px;top:9px;width:14px;height:14px}

.tabbar{position:absolute;left:0;right:0;bottom:0;height:93px;background:var(--tab);box-shadow:0 -4px 14px rgba(0,0,0,.07);display:flex;justify-content:space-around;padding:24px 20px 0}
.tab{display:flex;flex-direction:column;align-items:center;gap:8px;font:600 10px var(--ui);color:var(--sub);width:80px}
.tab svg{width:22px;height:22px;stroke:var(--sub);fill:none;stroke-width:2}
.tab--on{color:var(--pink)}.tab--on svg{stroke:var(--pink)}

.section-head{position:absolute;top:100px;left:19px;right:17px;display:flex;justify-content:space-between;align-items:center}
.section-head h2{font:400 24px var(--ui)}
.pill{background:var(--accent);color:#fff;font:600 11px var(--ui);padding:4px 14px;border-radius:12px}
.clips{position:absolute;top:140px;left:19px;right:0;height:122px;display:flex;gap:11px;overflow:hidden}
.clip{flex:0 0 131px;position:relative;border-radius:4px;overflow:hidden}
.clip__time{position:absolute;left:6px;bottom:6px;display:flex;align-items:center;gap:5px;color:#fff;font:600 13px var(--ui)}
.clip__time b{width:18px;height:18px;border-radius:50%;background:#fff;display:inline-flex;align-items:center;justify-content:center}
.clip--picked::after{content:"";position:absolute;inset:0;background:rgba(248,110,104,.82)}
.clip__tick{position:absolute;left:42px;top:38px;width:48px;height:40px;z-index:1;stroke:#fff;fill:none;stroke-width:5}
.gallery{position:absolute;top:307px;left:19px;right:17px;height:131px;border:2px dashed var(--fieldline);border-radius:6px;background:var(--field);display:flex;flex-direction:column;align-items:center;justify-content:center;gap:10px;color:var(--sub);font:400 18px var(--ui)}
.gallery svg{width:34px;height:38px;stroke:var(--sub);fill:none;stroke-width:2}
.picked{position:absolute;top:492px;left:30px;right:28px;height:357px;border-radius:12px;background:#fff;padding:10px;box-shadow:0 10px 30px rgba(0,0,0,.15)}
.picked__img{width:100%;height:100%;border-radius:8px;background:linear-gradient(170deg,#9fc7ea 0%,#c7dcea 25%,#8fbf4a 55%,#e7553f 85%,#c94032 100%)}
.picked__del{position:absolute;right:14px;top:14px;width:30px;height:30px;border-radius:50%;background:rgba(60,60,60,.75);display:flex;align-items:center;justify-content:center}
.picked__del svg{width:14px;height:16px;fill:#fff}
.comment{position:absolute;top:893px;left:19px;right:17px;height:131px;border:2px solid var(--fieldline);border-radius:8px;background:var(--field);padding:12px;color:var(--sub);font:400 16px var(--ui)}
.cta{position:absolute;left:138px;width:187px;height:45px;border-radius:23px;background:var(--accent);color:#fff;font:600 16px var(--ui);display:flex;align-items:center;justify-content:center;box-shadow:0 8px 16px rgba(247,81,106,.35)}
.cta--save{top:1049px}.cta--trim{top:680px}

.video{position:absolute;top:79px;left:0;right:0;height:258px;background:linear-gradient(170deg,#4a4a48 0%,#6d6a66 35%,#bdb7ae 65%,#8a847b 100%);display:flex;align-items:center;justify-content:center}
.video__play{width:48px;height:48px;border-radius:50%;border:3px solid #fff;display:flex;align-items:center;justify-content:center}
.tools{position:absolute;top:359px;left:19px;right:17px;display:flex;gap:13px}
.tool{flex:1;height:75px;border-radius:7px;background:var(--chip);color:var(--sub);font:400 12px var(--ui);display:flex;flex-direction:column;align-items:center;justify-content:center;gap:6px}
.tool svg{width:28px;height:28px;fill:var(--chipico)}
.tool--on{background:var(--accent);color:#fff}
.trim__title{position:absolute;top:478px;left:29px;font:400 24px var(--ui)}
.scale{position:absolute;top:526px;left:19px;right:17px;height:30px;font:400 12px var(--ui);color:var(--sub)}
.scale span{position:absolute;top:0}
.scale i{position:absolute;left:0;right:0;top:22px;border-top:4px dotted var(--sub);opacity:.6}
.strip{position:absolute;top:565px;left:19px;right:17px;height:54px;border-radius:4px;background:repeating-linear-gradient(90deg,#5a5753 0 30px,#8f8a82 30px 54px)}
.strip__sel{position:absolute;top:563px;left:19px;width:166px;height:58px;border:5px solid var(--pink);border-radius:5px;background:rgba(247,81,106,.15)}
.strip__sel::before,.strip__sel::after{content:"";position:absolute;top:14px;width:3px;height:20px;background:#fff}
.strip__sel::before{left:6px}.strip__sel::after{right:6px}
.playhead{position:absolute;top:538px;left:197px;width:2px;height:100px;background:var(--text)}
.playhead::before{content:"";position:absolute;left:-6px;top:-6px;border:7px solid transparent;border-top:9px solid var(--text)}
.trim__len{position:absolute;top:626px;left:80px;color:var(--pink);font:700 15px var(--ui)}
</style>
</head>
<body>
<svg width="0" height="0" style="position:absolute" aria-hidden="true">
  <symbol id="i-cal" viewBox="0 0 16 16"><path d="M2 3h12v11H2z M4 1h2v3H4z M10 1h2v3h-2z" /><path d="M3 6h10v7H3z" fill="rgba(0,0,0,.25)"/></symbol>
  <symbol id="i-pic" viewBox="0 0 16 16"><path d="M1 2h14v12H1zM3 12h10l-3-5-2 3-2-2z" fill-rule="evenodd"/></symbol>
  <symbol id="i-play" viewBox="0 0 16 16"><circle cx="8" cy="8" r="7.5"/><path d="M6 4.5l5 3.5-5 3.5z" fill="#555"/></symbol>
  <symbol id="i-menu" viewBox="0 0 24 20"><path d="M0 2h24M0 10h24M0 18h16" stroke="currentColor" stroke-width="2.4"/></symbol>
</svg>

<!-- LIGHT BOARD -->
<section class="board board--light">
  <h1 class="board__title">Light Version</h1>
  <span class="board__size">(1242 x 2208)</span>

  <div class="phone slot-a">
    <div class="status"><span>●●●●○ NETCO</span><span>1:20 PM</span><span>100%<i class="status__batt"></i></span></div>
    <div class="nav"><svg class="nav__menu" style="color:var(--text)"><use href="#i-menu"/></svg>
      <div class="nav__title"><svg class="ico" viewBox="0 0 14 22"><path d="M11 3L3 11l8 8"/></svg>December<svg class="ico" viewBox="0 0 14 22"><path d="M3 3l8 8-8 8"/></svg></div></div>
    <div class="toolbar"><div class="btn-fill">Auto fill</div><div class="viewas">View As
      <svg viewBox="0 0 26 26"><g fill="#f7516a"><rect x="1" y="1" width="11" height="11"/><rect x="14" y="1" width="11" height="11"/><rect x="1" y="14" width="11" height="11"/><rect x="14" y="14" width="11" height="11"/></g></svg>
      <svg viewBox="0 0 26 26"><g fill="#b8b8b8"><rect x="1" y="1" width="7" height="7"/><rect x="10" y="1" width="7" height="7"/><rect x="19" y="1" width="7" height="7"/><rect x="1" y="10" width="7" height="7"/><rect x="10" y="10" width="7" height="7"/><rect x="19" y="10" width="7" height="7"/><rect x="1" y="19" width="7" height="7"/><rect x="10" y="19" width="7" height="7"/><rect x="19" y="19" width="7" height="7"/></g></svg></div></div>
    <div class="grid grid--two">
      <div class="tile photo-a" role="img" aria-label="Photo of two children playing football on a path"><div class="tile__meta"><svg><use href="#i-cal"/></svg><span class="tile__num">3</span><span class="tile__dow">THU</span><svg class="tile__end"><use href="#i-pic"/></svg></div></div>
      <div class="tile photo-b" role="img" aria-label="Photo of children running through a sunny garden"><div class="tile__meta"><svg><use href="#i-cal"/></svg><span class="tile__num">4</span><span class="tile__dow">FRI</span><svg class="tile__end"><use href="#i-pic"/></svg></div></div>
      <div class="tile tile--day"><svg class="cal"><use href="#i-cal"/></svg><div class="day__num">5</div><div class="day__dow">SAT</div><div class="day__add"><i>+</i>ADD</div></div>
      <div class="tile photo-c" role="img" aria-label="Video still of children running on a green meadow"><div class="tile__meta"><svg><use href="#i-cal"/></svg><span class="tile__num">6</span><span class="tile__dow">SUN</span><svg class="tile__end"><use href="#i-play"/></svg></div></div>
      <div class="tile photo-c" role="img" aria-label="Photo of children outdoors"></div>
      <div class="tile tile--day"><svg class="cal"><use href="#i-cal"/></svg></div>
    </div>
    <nav class="tabbar">
      <div class="tab tab--on"><svg viewBox="0 0 22 22"><path d="M3 10l8-7 8 7v9H3z"/></svg>Home</div>
      <div class="tab"><svg viewBox="0 0 22 22"><circle cx="11" cy="11" r="9"/><path d="M9 7l5 4-5 4z"/></svg>Videos</div>
      <div class="tab"><svg viewBox="0 0 22 22"><circle cx="11" cy="11" r="9"/><path d="M11 6v10M6 11h10"/></svg>New</div>
      <div class="tab"><svg viewBox="0 0 22 22"><circle cx="11" cy="11" r="9"/><path d="M6 14h10M6 8l3 3 2-4 2 4 3-3v6H6z"/></svg>Upgrade PRO</div>
    </nav>
  </div>

  <div class="phone slot-b">
    <div class="status"><span>●●●●○ NETCO</span><span>1:20 PM</span><span>100%<i class="status__batt"></i></span></div>
    <div class="nav"><svg class="nav__menu" style="color:var(--text)"><use href="#i-menu"/></svg>
      <div class="nav__title"><svg class="ico" viewBox="0 0 14 22"><path d="M11 3L3 11l8 8"/></svg>December<svg class="ico" viewBox="0 0 14 22"><path d="M3 3l8 8-8 8"/></svg></div></div>
    <div class="toolbar"><div class="btn-fill">Auto fill</div><div class="viewas">View As
      <svg viewBox="0 0 26 26"><g fill="#b8b8b8"><rect x="1" y="1" width="11" height="11"/><rect x="14" y="1" width="11" height="11"/><rect x="1" y="14" width="11" height="11"/><rect x="14" y="14" width="11" height="11"/></g></svg>
      <svg viewBox="0 0 26 26"><g fill="#f7516a"><rect x="1" y="1" width="7" height="7"/><rect x="10" y="1" width="7" height="7"/><rect x="19" y="1" width="7" height="7"/><rect x="1" y="10" width="7" height="7"/><rect x="10" y="10" width="7" height="7"/><rect x="19" y="10" width="7" height="7"/><rect x="1" y="19" width="7" height="7"/><rect x="10" y="19" width="7" height="7"/><rect x="19" y="19" width="7" height="7"/></g></svg></div></div>
    <div class="grid grid--three">
      <div class="tile photo-a" role="img" aria-label="Photo of children playing football"><div class="tile__meta"><svg><use href="#i-cal"/></svg><span class="tile__num">3</span><span class="tile__dow">THU</span><svg class="tile__end"><use href="#i-pic"/></svg></div></div>
      <div class="tile photo-b" role="img" aria-label="Photo of children in a garden"><div class="tile__meta"><svg><use href="#i-cal"/></svg><span class="tile__num">3</span><span class="tile__dow">THU</span><svg class="tile__end"><use href="#i-pic"/></svg></div></div>
      <div class="tile tile--day"><svg class="cal"><use href="#i-cal"/></svg><div class="day__num">5</div><div class="day__dow">SAT</div><i class="plus">+</i></div>
      <div class="tile tile--day"><svg class="cal"><use href="#i-cal"/></svg><div class="day__num">6</div><div class="day__dow">SAT</div><i class="plus">+</i></div>
      <div class="tile photo-c" role="img" aria-label="Photo of children on a meadow"><div class="tile__meta"><svg><use href="#i-cal"/></svg><span class="tile__num">7</span><span class="tile__dow">THU</span><svg class="tile__end"><use href="#i-pic"/></svg></div></div>
      <div class="tile photo-a" role="img" aria-label="Photo of children playing football"><div class="tile__meta"><svg><use href="#i-cal"/></svg><span class="tile__num">8</span><span class="tile__dow">THU</span><svg class="tile__end"><use href="#i-pic"/></svg></div></div>
      <div class="tile photo-c" role="img" aria-label="Photo of children on a meadow"><div class="tile__meta"><svg><use href="#i-cal"/></svg><span class="tile__num">7</span><span class="tile__dow">THU</span><svg class="tile__end"><use href="#i-pic"/></svg></div></div>
      <div class="tile tile--day"><svg class="cal"><use href="#i-cal"/></svg><div class="day__num">9</div><div class="day__dow">SAT</div><i class="plus">+</i></div>
      <div class="tile photo-a" role="img" aria-label="Photo of children playing football"><div class="tile__meta"><svg><use href="#i-cal"/></svg><span class="tile__num">8</span><span class="tile__dow">THU</span><svg class="tile__end"><use href="#i-pic"/></svg></div></div>
      <div class="tile tile--day"><svg class="cal"><use href="#i-cal"/></svg><div class="day__num">12</div></div>
      <div class="tile photo-c" role="img" aria-label="Photo of children on a meadow"></div>
      <div class="tile photo-a" role="img" aria-label="Photo of children playing football"></div>
    </div>
    <nav class="tabbar">
      <div class="tab tab--on"><svg viewBox="0 0 22 22"><path d="M3 10l8-7 8 7v9H3z"/></svg>Home</div>
      <div class="tab"><svg viewBox="0 0 22 22"><circle cx="11" cy="11" r="9"/><path d="M9 7l5 4-5 4z"/></svg>Videos</div>
      <div class="tab"><svg viewBox="0 0 22 22"><circle cx="11" cy="11" r="9"/><path d="M11 6v10M6 11h10"/></svg>New</div>
      <div class="tab"><svg viewBox="0 0 22 22"><circle cx="11" cy="11" r="9"/><path d="M6 14h10M6 8l3 3 2-4 2 4 3-3v6H6z"/></svg>Upgrade PRO</div>
    </nav>
  </div>

  <p class="board__label label-a">2 Column View</p>
  <p class="board__label label-b">3 Column View</p>

  <div class="phone phone--tall slot-c">
    <div class="status"><span>●●●●○ NETCO</span><span>1:20 PM</span><span>100%<i class="status__batt"></i></span></div>
    <div class="nav"><svg class="nav__back ico" viewBox="0 0 14 22"><path d="M11 3L3 11l8 8"/></svg><div class="nav__title nav__title--small">Select your Daily Photos &amp; Videos</div></div>
    <div class="section-head"><h2>Most Recent Clip</h2><span class="pill">View All</span></div>
    <div class="clips">
      <div class="clip photo-c" role="img" aria-label="Clip of children jumping on grass"><span class="clip__time"><b>▶</b>00:26</span></div>
      <div class="clip photo-c clip--picked" role="img" aria-label="Selected clip of children jumping"><svg class="clip__tick" viewBox="0 0 48 40"><path d="M6 20l12 12L42 6"/></svg></div>
      <div class="clip photo-c" role="img" aria-label="Clip of children jumping on grass"><span class="clip__time"><b>▶</b>00:26</span></div>
      <div class="clip photo-c" role="img" aria-label="Clip of children outdoors"></div>
    </div>
    <div class="gallery"><svg viewBox="0 0 34 38"><path d="M3 2h18l9 9v25H3z M21 2v9h9"/><circle cx="24" cy="29" r="6"/><path d="M24 26v6M21 29h6"/></svg>Choose from Gallery</div>
    <div class="picked"><div class="picked__img" role="img" aria-label="Photo of girls playing with hoops in a park"></div><div class="picked__del"><svg viewBox="0 0 14 16"><path d="M1 3h12v1.5H1zM5 1h4v2H5zM2.5 5h9l-1 10h-7z"/></svg></div></div>
    <div class="comment">Add your comments or thoughts here! (Optional)</div>
    <div class="cta cta--save">Save</div>
  </div>

  <div class="phone slot-d">
    <div class="status"><span>●●●●○ NETCO</span><span>1:20 PM</span><span>100%<i class="status__batt"></i></span></div>
    <div class="nav"><svg class="nav__back ico" viewBox="0 0 14 22"><path d="M11 3L3 11l8 8"/></svg><div class="nav__title nav__title--small">Customize your Video</div></div>
    <div class="video" role="img" aria-label="Video still of a baby lying on a bed with toys"><div class="video__play"><svg width="18" height="20" viewBox="0 0 18 20"><path d="M3 1l14 9-14 9z" fill="#fff"/></svg></div></div>
    <div class="tools">
      <div class="tool tool--on"><svg viewBox="0 0 28 28"><circle cx="14" cy="14" r="12" fill="#fff"/><path d="M11 8l9 6-9 6z" fill="#f7516a"/></svg>Video</div>
      <div class="tool"><svg viewBox="0 0 28 28"><path d="M3 10h6l7-6v20l-7-6H3z"/><path d="M20 9a7 7 0 010 10M23 6a11 11 0 010 16" stroke="var(--chipico)" fill="none" stroke-width="2"/></svg>Audio</div>
      <div class="tool"><svg viewBox="0 0 28 28"><path d="M3 5h22v20H3zM7 2h3v5H7zM18 2h3v5h-3z"/><path d="M6 11h16v11H6z" fill="var(--chip)"/><path d="M8 13h3v3H8zM13 13h3v3h-3zM18 13h3v3h-3zM8 18h3v3H8zM13 18h3v3h-3z"/></svg>Date</div>
      <div class="tool"><svg viewBox="0 0 28 28"><path d="M14 1a8 8 0 018 8c0 6-8 13-8 13S6 15 6 9a8 8 0 018-8z"/><circle cx="14" cy="9" r="3" fill="var(--chip)"/><path d="M4 25h20v2H4z"/></svg>Location</div>
    </div>
    <h3 class="trim__title">Trim</h3>
    <div class="scale"><span style="left:0">0s</span><span style="left:119px">15s</span><span style="left:236px">30s</span><span style="left:354px">45s</span><i></i></div>
    <div class="strip" role="img" aria-label="Filmstrip of video frames"></div>
    <div class="strip__sel"></div>
    <div class="playhead"></div>
    <span class="trim__len">18s</span>
    <div class="cta cta--trim">Trim</div>
  </div>
</section>

<!-- DARK BOARD -->
<section class="board board--dark">
  <h1 class="board__title">Dark Version</h1>
  <span class="board__size">(1242 x 2208)</span>

  <div class="phone slot-a">
    <div class="status"><span>●●●●○ NETCO</span><span>1:20 PM</span><span>100%<i class="status__batt"></i></span></div>
    <div class="nav"><svg class="nav__menu" style="color:var(--text)"><use href="#i-menu"/></svg>
      <div class="nav__title"><svg class="ico" viewBox="0 0 14 22"><path d="M11 3L3 11l8 8"/></svg>December<svg class="ico" viewBox="0 0 14 22"><path d="M3 3l8 8-8 8"/></svg></div></div>
    <div class="toolbar"><div class="btn-fill">Auto fill</div><div class="viewas">View As
      <svg viewBox="0 0 26 26"><g fill="#f7516a"><rect x="1" y="1" width="11" height="11"/><rect x="14" y="1" width="11" height="11"/><rect x="1" y="14" width="11" height="11"/><rect x="14" y="14" width="11" height="11"/></g></svg>
      <svg viewBox="0 0 26 26"><g fill="#8a8da0"><rect x="1" y="1" width="7" height="7"/><rect x="10" y="1" width="7" height="7"/><rect x="19" y="1" width="7" height="7"/><rect x="1" y="10" width="7" height="7"/><rect x="10" y="10" width="7" height="7"/><rect x="19" y="10" width="7" height="7"/><rect x="1" y="19" width="7" height="7"/><rect x="10" y="19" width="7" height="7"/><rect x="19" y="19" width="7" height="7"/></g></svg></div></div>
    <div class="grid grid--two">
      <div class="tile photo-a" role="img" aria-label="Photo of two children playing football on a path"><div class="tile__meta"><svg><use href="#i-cal"/></svg><span class="tile__num">3</span><span class="tile__dow">THU</span><svg class="tile__end"><use href="#i-pic"/></svg></div></div>
      <div class="tile photo-b" role="img" aria-label="Photo of children running through a sunny garden"><div class="tile__meta"><svg><use href="#i-cal"/></svg><span class="tile__num">4</span><span class="tile__dow">FRI</span><svg class="tile__end"><use href="#i-pic"/></svg></div></div>
      <div class="tile tile--day"><svg class="cal"><use href="#i-cal"/></svg><div class="day__num">5</div><div class="day__dow">SAT</div><div class="day__add"><i>+</i>ADD</div></div>
      <div class="tile photo-c" role="img" aria-label="Video still of children running on a green meadow"><div class="tile__meta"><svg><use href="#i-cal"/></svg><span class="tile__num">6</span><span class="tile__dow">SUN</span><svg class="tile__end"><use href="#i-play"/></svg></div></div>
      <div class="tile photo-c" role="img" aria-label="Photo of children outdoors"></div>
      <div class="tile tile--day"><svg class="cal"><use href="#i-cal"/></svg></div>
    </div>
    <nav class="tabbar">
      <div class="tab tab--on"><svg viewBox="0 0 22 22"><path d="M3 10l8-7 8 7v9H3z"/></svg>Home</div>
      <div class="tab"><svg viewBox="0 0 22 22"><circle cx="11" cy="11" r="9"/><path d="M9 7l5 4-5 4z"/></svg>Videos</div>
      <div class="tab"><svg viewBox="0 0 22 22"><circle cx="11" cy="11" r="9"/><path d="M11 6v10M6 11h10"/></svg>New</div>
      <div class="tab"><svg viewBox="0 0 22 22"><circle cx="11" cy="11" r="9"/><path d="M6 14h10M6 8l3 3 2-4 2 4 3-3v6H6z"/></svg>Upgrade PRO</div>
    </nav>
  </div>

  <div class="phone slot-b">
    <div class="status"><span>●●●●○ NETCO</span><span>1:20 PM</span><span>100%<i class="status__batt"></i></span></div>
    <div class="nav"><svg class="nav__menu" style="color:var(--text)"><use href="#i-menu"/></svg>
      <div class="nav__title"><svg class="ico" viewBox="0 0 14 22"><path d="M11 3L3 11l8 8"/></svg>December<svg class="ico" viewBox="0 0 14 22"><path d="M3 3l8 8-8 8"/></svg></div></div>
    <div class="toolbar"><div class="btn-fill">Auto fill</div><div class="viewas">View As
      <svg viewBox="0 0 26 26"><g fill="#8a8da0"><rect x="1" y="1" width="11" height="11"/><rect x="14" y="1" width="11" height="11"/><rect x="1" y="14" width="11" height="11"/><rect x="14" y="14" width="11" height="11"/></g></svg>
      <svg viewBox="0 0 26 26"><g fill="#f7516a"><rect x="1" y="1" width="7" height="7"/><rect x="10" y="1" width="7" height="7"/><rect x="19" y="1" width="7" height="7"/><rect x="1" y="10" width="7" height="7"/><rect x="10" y="10" width="7" height="7"/><rect x="19" y="10" width="7" height="7"/><rect x="1" y="19" width="7" height="7"/><rect x="10" y="19" width="7" height="7"/><rect x="19" y="19" width="7" height="7"/></g></svg></div></div>
    <div class="grid grid--three">
      <div class="tile photo-a" role="img" aria-label="Photo of children playing football"><div class="tile__meta"><svg><use href="#i-cal"/></svg><span class="tile__num">3</span><span class="tile__dow">THU</span><svg class="tile__end"><use href="#i-pic"/></svg></div></div>
      <div class="tile photo-b" role="img" aria-label="Photo of children in a garden"><div class="tile__meta"><svg><use href="#i-cal"/></svg><span class="tile__num">3</span><span class="tile__dow">THU</span><svg class="tile__end"><use href="#i-pic"/></svg></div></div>
      <div class="tile tile--day"><svg class="cal"><use href="#i-cal"/></svg><div class="day__num">5</div><div class="day__dow">SAT</div><i class="plus">+</i></div>
      <div class="tile tile--day"><svg class="cal"><use href="#i-cal"/></svg><div class="day__num">6</div><div class="day__dow">SAT</div><i class="plus">+</i></div>
      <div class="tile photo-c" role="img" aria-label="Photo of children on a meadow"><div class="tile__meta"><svg><use href="#i-cal"/></svg><span class="tile__num">7</span><span class="tile__dow">THU</span><svg class="tile__end"><use href="#i-pic"/></svg></div></div>
      <div class="tile photo-a" role="img" aria-label="Photo of children playing football"><div class="tile__meta"><svg><use href="#i-cal"/></svg><span class="tile__num">8</span><span class="tile__dow">THU</span><svg class="tile__end"><use href="#i-pic"/></svg></div></div>
      <div class="tile photo-c" role="img" aria-label="Photo of children on a meadow"><div class="tile__meta"><svg><use href="#i-cal"/></svg><span class="tile__num">7</span><span class="tile__dow">THU</span><svg class="tile__end"><use href="#i-pic"/></svg></div></div>
      <div class="tile tile--day"><svg class="cal"><use href="#i-cal"/></svg><div class="day__num">9</div><div class="day__dow">SAT</div><i class="plus">+</i></div>
      <div class="tile photo-a" role="img" aria-label="Photo of children playing football"><div class="tile__meta"><svg><use href="#i-cal"/></svg><span class="tile__num">8</span><span class="tile__dow">THU</span><svg class="tile__end"><use href="#i-pic"/></svg></div></div>
      <div class="tile tile--day"><svg class="cal"><use href="#i-cal"/></svg><div class="day__num">12</div></div>
      <div class="tile photo-c" role="img" aria-label="Photo of children on a meadow"></div>
      <div class="tile photo-a" role="img" aria-label="Photo of children playing football"></div>
    </div>
    <nav class="tabbar">
      <div class="tab tab--on"><svg viewBox="0 0 22 22"><path d="M3 10l8-7 8 7v9H3z"/></svg>Home</div>
      <div class="tab"><svg viewBox="0 0 22 22"><circle cx="11" cy="11" r="9"/><path d="M9 7l5 4-5 4z"/></svg>Videos</div>
      <div class="tab"><svg viewBox="0 0 22 22"><circle cx="11" cy="11" r="9"/><path d="M11 6v10M6 11h10"/></svg>New</div>
      <div class="tab"><svg viewBox="0 0 22 22"><circle cx="11" cy="11" r="9"/><path d="M6 14h10M6 8l3 3 2-4 2 4 3-3v6H6z"/></svg>Upgrade PRO</div>
    </nav>
  </div>

  <p class="board__label label-a">2 Column View</p>
  <p class="board__label label-b">3 Column View</p>

  <div class="phone phone--tall slot-c">
    <div class="status"><span>●●●●○ NETCO</span><span>1:20 PM</span><span>100%<i class="status__batt"></i></span></div>
    <div class="nav"><svg class="nav__back ico" viewBox="0 0 14 22"><path d="M11 3L3 11l8 8"/></svg><div class="nav__title nav__title--small">Select your Daily Photos &amp; Videos</div></div>
    <div class="section-head"><h2>Most Recent Clip</h2><span class="pill">View All</span></div>
    <div class="clips">
      <div class="clip photo-c" role="img" aria-label="Clip of children jumping on grass"><span class="clip__time"><b>▶</b>00:26</span></div>
      <div class="clip photo-c clip--picked" role="img" aria-label="Selected clip of children jumping"><svg class="clip__tick" viewBox="0 0 48 40"><path d="M6 20l12 12L42 6"/></svg></div>
      <div class="clip photo-c" role="img" aria-label="Clip of children jumping on grass"><span class="clip__time"><b>▶</b>00:26</span></div>
      <div class="clip photo-c" role="img" aria-label="Clip of children outdoors"></div>
    </div>
    <div class="gallery" style="border-style:solid;border-color:var(--field)"><svg viewBox="0 0 34 38"><path d="M3 2h18l9 9v25H3z M21 2v9h9"/><circle cx="24" cy="29" r="6"/><path d="M24 26v6M21 29h6"/></svg>Choose from Gallery</div>
    <div class="picked" style="background:var(--field)"><div class="picked__img" role="img" aria-label="Photo of girls playing with hoops in a park"></div><div class="picked__del"><svg viewBox="0 0 14 16"><path d="M1 3h12v1.5H1zM5 1h4v2H5zM2.5 5h9l-1 10h-7z"/></svg></div></div>
    <div class="comment">Add your comments or thoughts here! (Optional)</div>
    <div class="cta cta--save">Save</div>
  </div>

  <div class="phone slot-d">
    <div class="status"><span>●●●●○ NETCO</span><span>1:20 PM</span><span>100%<i class="status__batt"></i></span></div>
    <div class="nav"><svg class="nav__back ico" viewBox="0 0 14 22"><path d="M11 3L3 11l8 8"/></svg><div class="nav__title nav__title--small">Customize your Video</div></div>
    <div class="video" role="img" aria-label="Video still of a baby lying on a bed with toys"><div class="video__play"><svg width="18" height="20" viewBox="0 0 18 20"><path d="M3 1l14 9-14 9z" fill="#fff"/></svg></div></div>
    <div class="tools">
      <div class="tool tool--on"><svg viewBox="0 0 28 28"><circle cx="14" cy="14" r="12" fill="#fff"/><path d="M11 8l9 6-9 6z" fill="#f7516a"/></svg>Video</div>
      <div class="tool"><svg viewBox="0 0 28 28"><path d="M3 10h6l7-6v20l-7-6H3z"/><path d="M20 9a7 7 0 010 10M23 6a11 11 0 010 16" stroke="var(--chipico)" fill="none" stroke-width="2"/></svg>Audio</div>
      <div class="tool"><svg viewBox="0 0 28 28"><path d="M3 5h22v20H3zM7 2h3v5H7zM18 2h3v5h-3z"/><path d="M6 11h16v11H6z" fill="var(--chip)"/><path d="M8 13h3v3H8zM13 13h3v3h-3zM18 13h3v3h-3zM8 18h3v3H8zM13 18h3v3h-3z"/></svg>Date</div>
      <div class="tool"><svg viewBox="0 0 28 28"><path d="M14 1a8 8 0 018 8c0 6-8 13-8 13S6 15 6 9a8 8 0 018-8z"/><circle cx="14" cy="9" r="3" fill="var(--chip)"/><path d="M4 25h20v2H4z"/></svg>Location</div>
    </div>
    <h3 class="trim__title">Trim</h3>
    <div class="scale"><span style="left:0">0s</span><span style="left:119px">15s</span><span style="left:236px">30s</span><span style="left:354px">45s</span><i></i></div>
    <div class="strip" role="img" aria-label="Filmstrip of video frames"></div>
    <div class="strip__sel"></div>
    <div class="playhead"></div>
    <span class="trim__len">18s</span>
    <div class="cta cta--trim">Trim</div>
  </div>

  <p class="thanks">Thank You !</p>
</section>
</body>
</html>
```